Stationery Design Needed: Business Card, Letterhead, Folder Design

Logo files attached I plan on using the standard us folder size 9x12 as well as standard US business card and letter head. I am the owner of Harborline Restorative Spine Associates, www.harborlinespinecare.example. I now have two locations, each with the same phone number and website. I enclosed my slogan and the information. I practice in an honest, ethical manor and place patients at a top priority. I want the designs to fit with my logo which symbolizes a blend of the symbol for ethical, honesty ( the peacock ) and the medusa ( medicine ) . I want to use the colors form my website blue, grey, silver to blend in and be cohesive and also match along the modern but natural colors along with blue and grey from the office. I want my cards and stationary to stand out

Target Market(s)

Lawyers, Surgeons, Primary Care Physicians Chiropractors

Industry/Entity Type

Business

Contact Information for Business Card

I want the cards and folders to stand out ...Bold colors I like the dark blue the best as I want this to be my signature color ...See below
I don t want too much white or too much aqua blue

Colors
3277b5

Requirements
Must have
• On Business cards... Must have logo, My name and practice, Two addresses, and my certifications from anesthesia and pain medicine .... web site easy to read for my target age audience 40 +
Nice to have
• slogan and other certifications
Should not have
• Confusing small to real letters ... so may need double sides but with all important on the front

```html
<!DOCTYPE html>
<html lang="en">
<head>
<meta charset="utf-8">
<title>Harborline Restorative Spine Associates — Letterhead</title>
<link rel="stylesheet" href="https://fonts.googleapis.com/css2?family=Open+Sans:wght@400;600;700&family=Cinzel:wght@400&display=swap">
<style>
  :root {
    --backdrop: #4ccbe9;
    --paper: #ffffff;
    --paper-tint: #d9f3fb;
    --brand-blue: #1f86c8;
    --brand-blue-dark: #1b6fae;
    --name-blue: #2a9ad6;
    --slogan-grey: #a9b0b6;
    --text-grey: #5d6670;
  }
  * { box-sizing: border-box; margin: 0; padding: 0; }
  html, body {
    width: 1200px; height: 784px; overflow: hidden;
    background: var(--backdrop);
    font-family: "Open Sans", Arial, sans-serif;
  }
  .letterhead {
    position: absolute; left: 314px; top: 22px;
    width: 572px; height: 740px;
    background: radial-gradient(ellipse 80% 70% at 55% 45%, var(--paper) 55%, var(--paper-tint) 100%);
    box-shadow: 0 6px 18px rgba(0, 60, 100, 0.25);
    overflow: hidden;
  }
  .brand {
    position: absolute; left: 30px; top: 26px;
    display: flex; align-items: flex-start; gap: 8px;
  }
  .brand-dot {
    width: 22px; height: 22px; border-radius: 50%;
    background: var(--brand-blue); margin-top: 2px;
  }
  .brand-name {
    color: var(--brand-blue); font-weight: 700;
    font-size: 12.5px; line-height: 1.2; text-transform: uppercase;
    letter-spacing: 0.3px; width: 150px;
  }
  .brand-web {
    margin-top: 3px; color: var(--brand-blue); font-weight: 700;
    font-size: 7px; letter-spacing: 0.2px; text-transform: uppercase;
    white-space: nowrap;
  }
  .slogan {
    position: absolute; right: 8px; top: 72px;
    font-family: "Cinzel", "Times New Roman", serif;
    font-size: 12px; color: var(--slogan-grey); letter-spacing: 0.6px;
    white-space: nowrap;
  }
  .header-rule {
    position: absolute; left: 170px; right: 0; top: 92px;
    height: 5px; background: var(--brand-blue-dark);
  }
  .footer {
    position: absolute; left: 10px; right: 10px; top: 604px;
    text-align: center; color: var(--text-grey);
  }
  .doctor-name {
    color: var(--name-blue); font-weight: 700; font-size: 12px; margin-bottom: 6px;
  }
  .credentials { font-size: 6.5px; line-height: 1.6; }
  .credentials p { white-space: nowrap; }
  .contact {
    margin-top: 5px; font-size: 7.5px; color: var(--text-grey);
    display: flex; justify-content: center; align-items: center; gap: 4px;
    white-space: nowrap;
  }
  .contact span { margin-right: 4px; }
  .contact svg { width: 7px; height: 7px; fill: var(--brand-blue); flex: none; }
  .bottom-tab {
    position: absolute; left: 150px; width: 165px; bottom: 0;
    height: 7px; background: var(--brand-blue-dark);
  }
</style>
</head>
<body>
  <main class="letterhead">
    <header>
      <div class="brand">
        <span class="brand-dot"></span>
        <div>
          <div class="brand-name">Harborline Restorative Spine Associates</div>
          <div class="brand-web">www.harborlinespinecare.example</div>
        </div>
      </div>
      <p class="slogan">Steady Care with Insight and Dependability</p>
      <div class="header-rule"></div>
    </header>

    <footer class="footer">
      <p class="doctor-name">Dr. Marcus T. Ellery, D.O.</p>
      <div class="credentials">
        <p>Certified by the Coastal Board of Pain Medicine | Certified by the Coastal Board of Anesthesiology</p>
        <p>Diplomate, Coastal Board of Pain Medicine | Diplomate, Coastal Board of Anesthesiology | Diplomate, Federated Osteopathic Medical Examiners</p>
        <p>Adjunct Faculty, Harwell College of Osteopathic Medicine | Meridian Pain Council Certified in Controlled Substances and Radiation Safety</p>
      </div>
      <p class="contact">
        <svg viewBox="0 0 10 10"><path d="M5 0a3.5 3.5 0 0 0-3.5 3.5C1.5 6 5 10 5 10s3.5-4 3.5-6.5A3.5 3.5 0 0 0 5 0zm0 5a1.5 1.5 0 1 1 0-3 1.5 1.5 0 0 1 0 3z"/></svg>
        <span>4820 Alder Crest Ave, Bayview, NJ 07990</span>
        <svg viewBox="0 0 10 10"><path d="M5 0a3.5 3.5 0 0 0-3.5 3.5C1.5 6 5 10 5 10s3.5-4 3.5-6.5A3.5 3.5 0 0 0 5 0zm0 5a1.5 1.5 0 1 1 0-3 1.5 1.5 0 0 1 0 3z"/></svg>
        <span>305 Meridian Rd., Suite 210, Lakeport, NJ 07920-1180</span>
        <svg viewBox="0 0 10 10"><path d="M2 0.5l2 2-1 1.3c.6 1.3 1.6 2.3 2.9 2.9l1.3-1 2 2-1.3 1.8C4.6 9.5.5 5.4 0.3 1.8z"/></svg>
        <span>555-014-7320</span>
        <svg viewBox="0 0 10 10"><path d="M2 0h5v3H2zM0 3.5h10V8H8v2H2V8H0zm3 4v1.8h4V7.5z"/></svg>
        <span>555-014-7321</span>
      </p>
    </footer>
    <div class="bottom-tab"></div>
  </main>
</body>
</html>
```